Redesign of the UI of a customer service platform

To improve the user experience of our customers, we need a new design for our agent interface of our customer service platform (quillvane.com).
The focus will be on the dashboard and the inbox screens (see attached) along with the common UI elements (Buttons, menu, fonts, forms...)
We want a simple and distinctive design

Target Market(s)

Worldwide

Industry/Entity Type

It Service

Number of Pages Required

3 page

Font styles to use
Sans Serif

Requirements
Must have
• New Onboarding page: this is a new page that is shown to user the first time they login to the platform. This will replace the current onboarding screen (setup SMS, Setup widget...etc)
• Dashboard page: to access important information and activate services (see screenshot from current site)
• Inbox page: to manage all the interactions with customers. (see screenshot from current site)
• UI elements (buttons, menus, forms, tables, fonts, color palette)

```html
<!DOCTYPE html>
<html lang="en">
<head>
<meta charset="utf-8">
<title>quillvane – Inbox</title>
<link href="https://fonts.googleapis.com/css2?family=Roboto:wght@400;500&display=swap" rel="stylesheet">
<style>
:root{
  --stage:#4a4a4a;--side:#1d3440;--side-top:#1f2a31;--side-active:#1a2a32;--side-line:#28434f;
  --header:#eef1fb;--red:#e4262a;--dark:#1f2d35;--yellow:#f5a90f;--grey:#e4e2e2;
  --list-bg:#f7f7f7;--blue:#2cb5ea;--green:#29b829;--text:#222;--muted:#555;--info:#1b3a48;--info-val:#9fb3bd;
}
*{box-sizing:border-box;margin:0;padding:0}
html,body{width:1200px;height:766px;overflow:hidden;background:var(--stage);font-family:'Roboto',sans-serif;color:var(--text)}
.app{position:absolute;left:31px;top:31px;width:1138px;height:703px;background:#fff;overflow:hidden}
.abs{position:absolute}
.sidebar{left:0;top:0;width:218px;height:703px;background:var(--side)}
.brand{left:0;top:0;width:218px;height:74px;background:var(--side-top)}
.brand-name{left:14px;top:22px;color:#fff;font-size:20px;font-weight:500;display:flex;align-items:center;gap:6px}
.brand-name i{width:16px;height:16px;border-radius:50%;background:#fff;display:block}
.burger{left:175px;top:21px;width:34px;height:34px;border-radius:50%;background:#3a4044;display:flex;flex-direction:column;justify-content:center;align-items:center;gap:4px}
.burger span{width:17px;height:2px;background:#e8542a}
.band{left:0;top:74px;width:218px;height:12px;background:#1b3b48}
.nav{left:0;top:86px;width:218px}
.nav-item{height:36px;display:flex;align-items:center;padding-left:16px;gap:10px;color:#fff;font-size:11px;border-bottom:1px solid var(--side-line)}
.nav-item.first{background:var(--side-active);height:35px}
.nav-item svg{width:14px;height:14px;fill:#fff}
.nav-item .chev{margin-left:auto;margin-right:12px;font-size:12px}
.header{left:218px;top:0;width:920px;height:74px;background:var(--header)}
.page-title{left:15px;top:26px;font-size:19px;display:flex;gap:10px;align-items:center}
.badge{position:absolute;width:12px;height:12px;border-radius:50%;font-size:7px;color:#fff;display:flex;align-items:center;justify-content:center}
.avatar-ph{border-radius:50%;background:radial-gradient(circle at 50% 40%,#c9a48a,#6b5144)}
.user{left:659px;top:37px;font-size:11px;transform:translateY(-50%)}
.avail{left:741px;top:27px;width:63px;height:21px;background:var(--green);color:#fff;font-size:10px;font-weight:500;display:flex;align-items:center;justify-content:center}
.help{left:830px;top:27px;width:20px;height:20px;border-radius:50%;background:var(--blue);color:#fff;font-size:12px;font-weight:500;display:flex;align-items:center;justify-content:center}
.list-col{left:233px;top:90px;width:262px;height:613px;background:var(--list-bg)}
.tabs{display:flex;height:50px}
.tab{background:var(--dark);color:#fff;font-size:10px;display:flex;align-items:center;justify-content:center;gap:8px;border-right:1px solid #2c3a42}
.tab.on{background:var(--red)}
.count{width:20px;height:20px;border-radius:50%;background:#fff;color:#222;font-size:9px;display:flex;align-items:center;justify-content:center}
.conv{position:relative;height:50px;background:var(--grey);border-top:1px solid #f2f2f2;font-size:10px}
.conv.on{background:var(--yellow)}
.conv .dot{position:absolute;left:10px;top:9px;width:32px;height:32px;border-radius:50%;background:var(--dark)}
.conv .num{position:absolute;left:53px;top:12px}
.conv .msg{position:absolute;left:47px;top:28px}
.conv .nm{position:absolute;left:90px;top:10px;font-weight:500}
.conv .ic{position:absolute;right:28px;top:12px}
.conv .time{position:absolute;right:10px;top:30px;font-size:9px}
.done-line{left:0;top:321px;width:262px;height:1px;background:#ddd}
.done-btn{left:108px;top:312px;width:47px;height:18px;border:1px solid #999;background:#fff;font-size:10px;display:flex;align-items:center;justify-content:center}
.no-done{left:0;top:349px;width:262px;text-align:center;font-size:8.5px}
.chat-title{left:510px;top:95px;height:22px;display:flex;align-items:center;gap:10px;font-size:12.5px;font-weight:500}
.chat-title i{width:8px;height:8px;border-radius:50%;background:var(--red);display:block}
.btn{height:22px;color:#fff;font-size:10px;font-weight:500;display:flex;align-items:center;justify-content:center;gap:6px}
.meta-bar{left:506px;top:121px;width:612px;height:22px;background:#e8e8e8;font-size:8.5px;display:flex;align-items:center;justify-content:space-between;padding:0 10px}
.msgs{left:506px;top:143px;width:612px;height:223px;border:1px solid #e6e6e6;border-top:0}
.compose{left:506px;top:366px;width:612px;height:85px;background:#e8e8e8}
.input{left:8px;top:8px;width:597px;height:47px;background:#fff;font-size:8.5px;color:#777;padding:8px 7px}
.emoji{position:absolute;top:62px;width:16px;height:16px;border-radius:50%;border:1px solid var(--blue)}
.dtabs{left:506px;top:460px;display:flex;height:31px}
.dtab{background:var(--dark);color:#fff;font-size:8.5px;display:flex;align-items:center;justify-content:center;gap:5px;border-right:1px solid #33434b}
.dtab.on{background:var(--yellow)}
.details{left:506px;top:491px;width:612px;height:212px;border:1px solid #e6e6e6}
.line{position:absolute;left:27px;font-size:8.5px;color:var(--muted)}
.line svg{position:absolute;left:-20px;top:0;width:9px;height:9px;fill:#666}
.info{left:929px;top:503px;width:174px;height:187px;background:var(--info);color:#fff;font-size:10px;padding:27px 14px 0}
.info p{height:22.4px}
.info span{color:var(--info-val)}
</style>
</head>
<body>
<div class="app">
  <aside class="abs sidebar">
    <div class="abs brand">
      <div class="abs brand-name"><i></i>quillvane</div>
      <div class="abs burger"><span></span><span></span><span></span></div>
    </div>
    <div class="abs band"></div>
    <nav class="abs nav">
      <div class="nav-item first"><svg viewBox="0 0 16 16"><path d="M8 2a7 7 0 0 0-7 7v3h14V9a7 7 0 0 0-7-7zm0 8a1.5 1.5 0 1 1 0-3 1.5 1.5 0 0 1 0 3z"/></svg>Dashboard<span class="chev">›</span></div>
      <div class="nav-item"><svg viewBox="0 0 16 16"><path d="M3 3h10l2 6v4H1V9zm1 6h3l1 2 1-2h3l-1.4-4H5.4z"/></svg>Inbox</div>
      <div class="nav-item"><svg viewBox="0 0 16 16"><path d="M9 1l6 6-8 8-6-6V1zM4 4a1 1 0 1 0 0 .1z"/></svg>Tickets</div>
      <div class="nav-item"><svg viewBox="0 0 16 16"><circle cx="5" cy="5" r="2.5"/><circle cx="11" cy="5" r="2.5"/><path d="M0 13c0-3 2-5 5-5s5 2 5 5zm8 0c0-1.5-.4-3-1.3-4 2.5-.8 8.3 0 8.3 4z"/></svg>Clients</div>
      <div class="nav-item"><svg viewBox="0 0 16 16"><path d="M8 2a7 7 0 0 0-7 7v3h14V9a7 7 0 0 0-7-7zm0 8a1.5 1.5 0 1 1 0-3 1.5 1.5 0 0 1 0 3z"/></svg>Reports</div>
      <div class="nav-item"><svg viewBox="0 0 16 16"><path d="M7 1h2l.4 2 1.6.8 1.7-1.2 1.4 1.4-1.2 1.7.8 1.6 2 .4v2l-2 .4-.8 1.6 1.2 1.7-1.4 1.4-1.7-1.2-1.6.8L9 15H7l-.4-2-1.6-.8-1.7 1.2-1.4-1.4 1.2-1.7L2.3 9 1 9V7l2-.4.8-1.6-1.2-1.7 1.4-1.4L5.7 3 7.3 2.2zm1 4.5a2.5 2.5 0 1 0 0 5 2.5 2.5 0 0 0 0-5z"/></svg>Settings</div>
    </nav>
  </aside>

  <header class="abs header">
    <div class="abs page-title"><svg width="14" height="12" viewBox="0 0 16 14"><path d="M3 1h10l2 6v6H1V7zm1 6h3l1 2 1-2h3l-1.4-4H5.4z" fill="#222"/></svg>Inbox</div>
    <div class="abs" style="left:500px;top:33px"><svg width="17" height="13" viewBox="0 0 17 13"><rect width="17" height="13" rx="1.5" fill="#333"/><path d="M1 1l7.5 6L16 1" stroke="#eef1fb" stroke-width="1.4" fill="none"/></svg><span class="badge" style="left:10px;top:-7px;background:var(--red)">4</span></div>
    <div class="abs" style="left:552px;top:31px"><svg width="18" height="18" viewBox="0 0 16 16"><path d="M9 1l6 6-8 8-6-6V1z" fill="#333"/></svg><span class="badge" style="left:13px;top:-5px;background:var(--yellow)">1</span></div>
    <div class="abs avatar-ph" role="img" aria-label="Agent profile photo" style="left:603px;top:13px;width:48px;height:48px"></div>
    <div class="abs user">Dale Orvik&nbsp;&nbsp;&nbsp;⌄</div>
    <div class="abs avail">Available</div>
    <div class="abs help">?</div>
  </header>

  <section class="abs list-col">
    <div class="tabs">
      <div class="tab on" style="width:86px">Agent <span class="count">4</span></div>
      <div class="tab" style="width:88px">Department</div>
      <div class="tab" style="width:88px">Account <span class="count">5</span></div>
    </div>
    <div class="conv on" style="margin-top:4px;border-top:0"><i class="dot"></i><span class="num">#4</span><span class="msg">Hello</span><span class="nm">Maren Holtwick</span><span class="ic">💬</span><span class="time">21 days ago</span></div>
    <div class="conv"><i class="dot"></i><span class="num">#3</span><span class="msg">Hello</span><span class="nm">Tova Brennick</span><span class="ic">💬</span><span class="time">10 days ago</span></div>
    <div class="conv"><i class="dot"></i><span class="num">#2</span><span class="msg">Hello</span><span class="nm">Ines Carrowmore</span><span class="ic">💬</span><span class="time">a month ago</span></div>
    <div class="conv"><i class="dot"></i><span class="num">#1</span><span class="msg">Hello</span><span class="nm">Dale Orvik</span><span class="ic">💬</span><span class="time">21 days ago</span></div>
    <div class="abs done-line"></div>
    <div class="abs done-btn">Done</div>
    <div class="abs no-done">No Done Clients</div>
  </section>

  <div class="abs chat-title"><i></i>#4 - Maren Holtwick</div>
  <div class="abs btn" style="left:930px;top:95px;width:56px;background:var(--yellow)">✖ Close</div>
  <div class="abs btn" style="left:990px;top:95px;width:74px;background:var(--blue)">➤ Transfer</div>
  <div class="abs btn" style="left:1067px;top:95px;width:51px;background:var(--red)">⊘ Ban</div>
  <div class="abs meta-bar"><span>⊕&nbsp; More Details</span><span>▣&nbsp; Save Transcript</span></div>
  <div class="abs msgs">
    <div class="abs avatar-ph" role="img" aria-label="Customer photo" style="left:7px;top:10px;width:32px;height:32px"></div>
    <div class="abs" style="left:51px;top:10px;font-size:9.5px;line-height:15px">#4<br>Hello</div>
    <div class="abs" style="left:483px;top:38px;font-size:9.5px;line-height:18px;text-align:left">
      <span style="color:var(--blue)">🗨</span>&nbsp; hi<br><span style="font-size:8.5px">21 days ago</span></div>
    <div class="abs avatar-ph" role="img" aria-label="Customer photo" style="left:545px;top:31px;width:32px;height:32px"></div>
  </div>
  <div class="abs compose">
    <div class="abs input">Type your message here.....</div>
    <span class="emoji" style="left:10px"></span><span class="emoji" style="left:29px"></span><span class="emoji" style="left:48px"></span><span class="emoji" style="left:67px"></span><span class="emoji" style="left:86px"></span>
  </div>
  <div class="abs dtabs">
    <div class="dtab on" style="width:62px">ⓘ Details</div>
    <div class="dtab" style="width:60px">◆ Ticket</div>
    <div class="dtab" style="width:66px">▤ History</div>
  </div>
  <section class="abs details">
    <div class="abs" style="left:27px;top:21px;font-size:11.5px;font-weight:500">Maren Holtwick</div>
    <div class="line" style="top:51px">hello@pinecrestlab.com</div>
    <div class="line" style="top:68px">+91 55501 23400</div>
    <div class="line" style="top:87px">www.pinecrestlab.com</div>
    <div class="line" style="top:107px;line-height:15.5px">48 Larkfield Row, Room No: 12<br>London<br>United Kingdom</div>
    <div class="abs btn" style="left:25px;top:162px;width:55px;height:21px;background:var(--blue)">✎ Edit</div>
    <div class="abs" style="left:8px;top:23px;font-size:8px;color:#666;line-height:17.5px">👤<br>&nbsp;</div>
    <div class="abs" style="left:8px;top:53px;font-size:8px;color:#666;line-height:18.5px">✉<br>☎<br>◉<br>⚲</div>
  </section>
  <div class="abs info">
    <p>IP Address: <span>192.168.0.234</span></p>
    <p>Country: <span>India</span></p>
    <p>Page: <span>www.pinecrestlab.com</span></p>
    <p>Browser: <span>Nimbus Browser</span></p>
    <p>Device: <span>Desktop</span></p>
    <p>OS: <span>Orbit OS 10</span></p>
  </div>
</div>
</body>
</html>
```